CLEVER, EYE catching stationary for oil & gas technology company
Kelvor Subsurface Group
I need double sided standard sized Business Card [3.5" x 2"]
eurostile LT ExtendedTwo
Simple
Darren Holloway
Managing Partner
#22, 4307 - 3rd Avenue
Nisku, AB
R4K 2M9
darren.holloway@kelvor.ca
www.kelvor.ca
Business cards will have rounded corners.
Back of business card we would like to see the Kelvor logo on a black back ground (but are open to other suggestions)
Centered on the back bottom part of card it should state: "Kelvor Subsurface Group Inc."

```html
<!DOCTYPE html>
<html lang="en">
<head>
<meta charset="utf-8">
<title>Kelvor Subsurface Group – Business Card</title>
<link rel="stylesheet" href="https://fonts.googleapis.com/css2?family=Michroma&display=swap">
<style>
  :root {
    --page-bg: #e4e6e9;
    --card-black: #141414;
    --card-black-deep: #070707;
    --brand-blue: #1f7fd4;
    --brand-blue-light: #3aa0ee;
    --brand-blue-dark: #0f5aa8;
    --brand-orange: #f26a1b;
    --text-white: #f4f6f8;
    --text-soft: #c9ced4;
    --card-radius: 24px;
  }
  * { margin: 0; padding: 0; box-sizing: border-box; }
  html, body {
    width: 1200px;
    height: 1009px;
    overflow: hidden;
    background: var(--page-bg);
    font-family: "Michroma", "Eurostile", sans-serif;
  }
  .sheet {
    width: 1200px;
    height: 1009px;
    display: flex;
    flex-direction: column;
    align-items: center;
    justify-content: center;
    gap: 36px;
  }
  .card {
    position: relative;
    width: 800px;
    height: 457px;
    border-radius: var(--card-radius);
    overflow: hidden;
    background: radial-gradient(ellipse at 60% 30%, var(--card-black) 0%, var(--card-black-deep) 100%);
    box-shadow: 0 10px 26px rgba(0,0,0,0.22);
  }
  .card-art {
    position: absolute;
    inset: 0;
    width: 100%;
    height: 100%;
  }

  /* Front */
  .contact-block {
    position: absolute;
    left: 34px;
    top: 38px;
    color: var(--text-white);
    font-style: normal;
    font-size: 12px;
    line-height: 24px;
    letter-spacing: 0.02em;
  }
  .wordmark {
    position: absolute;
    left: 400px;
    top: 150px;
    display: flex;
    align-items: center;
    gap: 16px;
    color: var(--brand-orange);
  }
  .wordmark-dot {
    width: 30px;
    height: 30px;
    border-radius: 50%;
    background: var(--brand-blue);
    flex: none;
  }
  .wordmark-text { line-height: 1; }
  .wordmark-name {
    display: block;
    font-size: 52px;
    letter-spacing: 0.02em;
  }
  .wordmark-sub {
    display: block;
    margin-top: 10px;
    font-size: 16px;
    text-align: right;
  }
  .person {
    position: absolute;
    right: 34px;
    bottom: 30px;
    text-align: right;
    color: var(--text-white);
    font-size: 12px;
    line-height: 22px;
    letter-spacing: 0.04em;
  }
  .person-name { font-size: 14px; }

  /* Back */
  .back-mark {
    position: absolute;
    left: 0;
    right: 0;
    top: 120px;
    display: flex;
    flex-direction: column;
    align-items: center;
    gap: 18px;
  }
  .back-dot {
    width: 64px;
    height: 64px;
    border-radius: 50%;
    background: var(--brand-blue);
  }
  .back-name {
    color: var(--brand-orange);
    font-size: 34px;
    letter-spacing: 0.04em;
  }
  .back-web {
    position: absolute;
    left: 0;
    right: 0;
    top: 292px;
    text-align: center;
    color: var(--brand-orange);
    font-size: 13px;
    letter-spacing: 0.6em;
    padding-left: 0.6em;
  }
  .back-legal {
    position: absolute;
    left: 0;
    right: 0;
    bottom: 38px;
    text-align: center;
    color: var(--text-soft);
    font-size: 12px;
    letter-spacing: 0.08em;
  }
</style>
</head>
<body>
<main class="sheet">

  <section class="card card-front" aria-label="Business card front">
    <svg class="card-art" viewBox="0 0 800 457" aria-hidden="true">
      <defs>
        <linearGradient id="blueField" x1="0" y1="0" x2="1" y2="1">
          <stop offset="0" stop-color="#3aa0ee"/>
          <stop offset="0.55" stop-color="#1f7fd4"/>
          <stop offset="1" stop-color="#0f5aa8"/>
        </linearGradient>
      </defs>
      <path d="M0,0 L230,0 C300,205 520,335 800,352 L800,457 L0,457 Z" fill="url(#blueField)"/>
      <path d="M248,0 C318,196 532,320 800,336" fill="none" stroke="#f26a1b" stroke-width="11"/>
      <path d="M274,0 C344,186 548,304 800,318" fill="none" stroke="#1f7fd4" stroke-width="3"/>
    </svg>

    <address class="contact-block">
      #22, 4307 - 3rd Avenue<br>
      Nisku, AB R4K 2M9<br>
      T 780 555 0142<br>
      darren.holloway@kelvor.ca
    </address>

    <div class="wordmark">
      <span class="wordmark-dot"></span>
      <span class="wordmark-text">
        <span class="wordmark-name">KELVOR</span>
        <span class="wordmark-sub">Subsurface Group</span>
      </span>
    </div>

    <div class="person">
      <div class="person-name">Darren Holloway</div>
      <div class="person-title">Managing Partner</div>
    </div>
  </section>

  <section class="card card-back" aria-label="Business card back">
    <div class="back-mark">
      <span class="back-dot"></span>
      <span class="back-name">Kelvor</span>
    </div>
    <div class="back-web">www.kelvor.ca</div>
    <div class="back-legal">Kelvor Subsurface Group Inc.</div>
  </section>

</main>
</body>
</html>
```